Business Card Design Project

Basic business card with minimal details. I just need company name, email & web address, telephone and my name.
I would like the back of the card to be grey with my logo & company name centred.

Target Market(s)

Architects
Builders
Property Developers

Industry/Entity Type

Business

Font styles to use
Sans Serif

Colors

Designer to choose colors to be used in the design.

Requirements
Must have
• Venture Frame
Marcus Hadley - Director
M: 0452 913084
E: marcus@ventureframe.com.au
W: www.ventureframe.com.au
Should not have
• No other images or pictures

```html
<!DOCTYPE html>
<html lang="en">
<head>
<meta charset="utf-8">
<title>Venture Frame – Business Card</title>
<link rel="stylesheet" href="https://fonts.googleapis.com/css2?family=Exo+2:wght@300;400&display=swap">
<style>
  :root {
    --backdrop: #5ed0be;
    --card: #e6e6e4;
    --card-edge: #bfe9dc;
    --brand-red: #c0213a;
    --ink: #3d4250;
    --ink-soft: #5b606b;
  }
  * { margin: 0; padding: 0; box-sizing: border-box; }
  html, body {
    width: 1200px;
    height: 1050px;
    overflow: hidden;
    background: var(--backdrop);
    font-family: "Exo 2", "Helvetica Neue", Arial, sans-serif;
    color: var(--ink);
  }
  .canvas {
    position: relative;
    width: 1200px;
    height: 1050px;
  }
  .card {
    position: absolute;
    left: 250px;
    width: 700px;
    height: 400px;
    background: var(--card);
    border-bottom: 6px solid var(--card-edge);
    box-shadow: 0 10px 24px rgba(0, 0, 0, 0.12);
  }
  .card--front { top: 90px; }
  .card--back  { top: 560px; }

  .brand-square {
    display: inline-block;
    background: var(--brand-red);
  }

  /* Front */
  .front-head {
    position: absolute;
    left: 64px;
    top: 70px;
    display: flex;
    align-items: flex-start;
    gap: 28px;
  }
  .front-head .brand-square { width: 60px; height: 60px; }
  .holder-name {
    font-size: 40px;
    font-weight: 300;
    line-height: 1.05;
    letter-spacing: 0.5px;
  }
  .holder-role {
    font-size: 22px;
    font-weight: 300;
    color: var(--ink-soft);
    margin-top: 4px;
  }
  .front-brand {
    position: absolute;
    left: 64px;
    top: 150px;
    font-size: 13px;
    font-weight: 400;
    letter-spacing: 3px;
    text-transform: uppercase;
    color: var(--ink);
  }
  .contact {
    position: absolute;
    left: 152px;
    top: 222px;
    display: grid;
    grid-template-columns: 96px auto;
    row-gap: 10px;
    font-size: 18px;
    font-weight: 300;
  }
  .contact dt { color: var(--ink-soft); }
  .web {
    position: absolute;
    left: 248px;
    top: 318px;
    font-size: 16px;
    font-weight: 300;
    color: var(--ink-soft);
  }

  /* Back */
  .back-lockup {
    position: absolute;
    inset: 0;
    display: flex;
    align-items: center;
    justify-content: center;
    gap: 26px;
  }
  .back-lockup .brand-square { width: 64px; height: 64px; }
  .back-name {
    font-size: 46px;
    font-weight: 300;
    letter-spacing: 3px;
    text-transform: uppercase;
    color: var(--ink);
  }
</style>
</head>
<body>
<main class="canvas">
  <section class="card card--front" aria-label="Business card front">
    <div class="front-head">
      <span class="brand-square" aria-hidden="true"></span>
      <div>
        <h1 class="holder-name">Marcus Hadley</h1>
        <p class="holder-role">director</p>
      </div>
    </div>
    <p class="front-brand">Venture Frame</p>
    <dl class="contact">
      <dt>Mobile:</dt><dd>0452 913084</dd>
      <dt>E-mail:</dt><dd>marcus@ventureframe.com.au</dd>
    </dl>
    <p class="web">www.ventureframe.com.au</p>
  </section>

  <section class="card card--back" aria-label="Business card back">
    <div class="back-lockup">
      <span class="brand-square" aria-hidden="true"></span>
      <h2 class="back-name">Venture Frame</h2>
    </div>
  </section>
</main>
</body>
</html>
```